Quillmoor Farm Organic Flower Farm, Farmer Florist

I am a flower grower and florist, so I do everything from the field to the vase. I want to include my website, phone, email and instagram

```html
<!DOCTYPE html>
<html lang="en">
<head>
<meta charset="utf-8">
<title>Quillmoor Farm – Business Card</title>
<link rel="stylesheet" href="https://fonts.googleapis.com/css2?family=Cinzel:wght@400;500&family=Cormorant+Garamond:wght@500&family=Great+Vibes&display=swap">
<style>
  :root {
    --backdrop: #dcdcdc;
    --card: #f9eef0;
    --plum: #5a1f24;
    --coral: #ee8a8c;
    --petal-light: #ffffff;
    --petal-mid: #efe3e6;
    --shadow: rgba(60, 40, 45, 0.18);
  }
  * { box-sizing: border-box; margin: 0; padding: 0; }
  html, body {
    width: 1200px;
    height: 1067px;
    overflow: hidden;
    background: var(--backdrop);
  }
  .sheet {
    width: 1200px;
    height: 1067px;
    display: flex;
    flex-direction: column;
    align-items: center;
    justify-content: center;
    gap: 60px;
  }
  .card {
    position: relative;
    width: 760px;
    height: 434px;
    border-radius: 34px;
    background: var(--card);
    box-shadow: 0 8px 22px var(--shadow);
    overflow: hidden;
  }
  /* Front */
  .card-front {
    display: flex;
    flex-direction: column;
    align-items: center;
    justify-content: center;
    gap: 18px;
  }
  .brand-mark {
    width: 26px;
    height: 26px;
    border-radius: 50%;
    background: var(--plum);
  }
  .brand-name {
    font-family: "Cinzel", serif;
    font-weight: 500;
    font-size: 58px;
    letter-spacing: 6px;
    color: var(--plum);
  }
  /* Back */
  .floral-field {
    position: absolute;
    inset: 0;
    background:
      radial-gradient(circle at 72% 22%, var(--petal-light) 0 10%, transparent 26%),
      radial-gradient(circle at 30% 40%, var(--petal-light) 0 9%, transparent 24%),
      radial-gradient(circle at 12% 70%, var(--petal-light) 0 7%, transparent 20%),
      linear-gradient(180deg, var(--petal-mid) 0%, var(--card) 70%);
    opacity: 0.9;
  }
  .card-back .content {
    position: absolute;
    left: 0;
    right: 0;
    top: 100px;
    display: flex;
    flex-direction: column;
    align-items: center;
  }
  .owner-name {
    font-family: "Great Vibes", cursive;
    font-size: 92px;
    color: var(--plum);
    line-height: 1.1;
    margin-bottom: 34px;
  }
  .contact-list {
    list-style: none;
    display: flex;
    flex-direction: column;
    align-items: center;
    gap: 6px;
    font-family: "Cormorant Garamond", serif;
    font-weight: 500;
    font-size: 18px;
    letter-spacing: 2px;
    text-transform: uppercase;
    color: var(--coral);
  }
  .contact-social {
    display: flex;
    align-items: center;
    gap: 10px;
  }
  .social-dot {
    width: 14px;
    height: 14px;
    border-radius: 50%;
    border: 2px solid var(--plum);
  }
</style>
</head>
<body>
  <main class="sheet">
    <section class="card card-front" aria-label="Card front">
      <span class="brand-mark" aria-hidden="true"></span>
      <h1 class="brand-name">Quillmoor</h1>
    </section>

    <section class="card card-back" aria-label="Card back">
      <div class="floral-field" role="img" aria-label="Soft white paper roses and leaves in a pale blush floral arrangement"></div>
      <div class="content">
        <p class="owner-name">Mara Quill</p>
        <ul class="contact-list">
          <li>555-2468-1357</li>
          <li>info@quillmoor.com</li>
          <li>www.quillmoor.com</li>
          <li class="contact-social"><span class="social-dot" aria-hidden="true"></span>www.snapleaf.net/quillmoorfarm</li>
        </ul>
      </div>
    </section>
  </main>
</body>
</html>
```